Storm Restoration Contractor needs a professional letterhead design

Looking for a professional letterhead design. Not looking for your cheapo MS Word standard ones that are readily available. Dont want it to be cookie cutter look like ones readily available online. We just recently changed our logo and want to freshen up all our documents. Our company handles restoring a property back to a pre-loss condition after a storm damages it. For example, wind, hail, flood, fire losses.

Target Market(s)

Property Owners, Homeowners, Property Owners, Commercial Property Owners, Property Management Companies

Industry/Entity Type

Construction Company

Requirements
Must have
• Professional, Use 1 of 2 logo options
• Storm Restoration, Roofing, Siding, Windows

```html
<!DOCTYPE html>
<html lang="en">
<head>
<meta charset="utf-8">
<title>Stormline Renewal Letterhead</title>
<link href="https://fonts.googleapis.com/css2?family=Open+Sans:wght@400;700&display=swap" rel="stylesheet">
<style>
  :root {
    --brand-blue: #1b78b9;
    --ink: #3a3a3a;
    --paper: #ffffff;
    --watermark: #eeeeee;
  }
  * { box-sizing: border-box; margin: 0; padding: 0; }
  html, body { width: 1017px; height: 1200px; overflow: hidden; background: var(--paper); }
  .letterhead {
    position: relative;
    width: 1017px;
    height: 1200px;
    background: var(--paper);
    font-family: "Open Sans", Arial, sans-serif;
    color: var(--ink);
    overflow: hidden;
  }
  .brand {
    position: absolute;
    top: 110px;
    left: 0;
    right: 0;
    display: flex;
    align-items: center;
    justify-content: center;
    gap: 16px;
  }
  .brand-dot {
    width: 58px;
    height: 58px;
    border-radius: 50%;
    border: 6px solid var(--brand-blue);
  }
  .brand-name {
    font-size: 34px;
    font-weight: 700;
    color: var(--brand-blue);
    letter-spacing: 1px;
    text-transform: uppercase;
  }
  .recipient {
    position: absolute;
    top: 340px;
    left: 130px;
    font-size: 14px;
    line-height: 1.35;
  }
  .letter-body {
    position: absolute;
    top: 450px;
    left: 130px;
    width: 700px;
    font-size: 14px;
    line-height: 1.4;
  }
  .letter-body p { margin-bottom: 22px; }
  .letter-body .closing { margin-top: 30px; }
  .signature {
    position: absolute;
    top: 920px;
    left: 130px;
    font-size: 14px;
    line-height: 1.35;
  }
  .watermark {
    position: absolute;
    right: -60px;
    bottom: 90px;
    width: 360px;
    height: 360px;
    border-radius: 50%;
    border: 34px solid var(--watermark);
  }
  .footer-band {
    position: absolute;
    left: 0;
    right: 0;
    bottom: 70px;
    height: 78px;
    background: var(--brand-blue);
    color: #ffffff;
    display: flex;
    align-items: center;
    justify-content: center;
    gap: 60px;
    font-size: 13px;
    line-height: 1.4;
  }
  .contact-lines { display: flex; flex-direction: column; gap: 2px; }
  .contact-line { display: flex; align-items: center; gap: 10px; }
  .contact-line svg { width: 13px; height: 13px; fill: #ffffff; }
</style>
</head>
<body>
<main class="letterhead">
  <header class="brand">
    <span class="brand-dot"></span>
    <span class="brand-name">Stormline Renewal</span>
  </header>

  <address class="recipient" style="font-style:normal">
    Mr. Daniel Hart<br>
    Managing Director<br>
    Northgate Capital<br>
    42 W Oak Avenue<br>
    USA
  </address>

  <section class="letter-body">
    <p>Lorem ipsum dolor sit amet, consectetuer adipiscing elit. Nam cursus. Morbi ut mi. Nullam enim leo, egestas id, condimentum at, laoreet mattis, massa. Sed eleifend nonummy diam. Praesent mauris ante, elementum et, bibendum at, posuere sit amet, nibh. Duis tincidunt lectus quis dui viverra vestibulum.</p>
    <p>Suspendisse vulputate aliquam dui. Nulla elementum dui ut augue. Aliquam vehicula mi at mauris. Maecenas placerat, nisl at consequat rhoncus, sem nunc gravida justo, quis eleifend arcu velit quis lacus. Morbi magna magna, tincidunt a, mattis non, imperdiet vitae, tellus. Sed odio est, auctor ac, sollicitudin in, consequat vitae, orci. Fusce id felis. Vivamus sollicitudin.</p>
    <p>Metus eget eros. Pellentesque habitant morbi tristique senectus et netus et malesuada fames ac turpis egestas. In posuere felis nec tortor. Pellentesque faucibus. Ut accumsan ultricies elit. Maecenas at justo id velit placerat molestie. Donec dictum lectus non odio. Cras a ante vitae enim iaculis aliquam.</p>
    <p>Mauris nunc quam, venenatis nec, euismod sit amet, egestas placerat, est. Pellentesque habitant morbi tristique senectus et netus et malesuada fames ac turpis egestas. Cras id elit. Integer quis urna. Ut ante enim, dapibus malesuada, fringilla eu, condimentum quis, tellus. Aenean porttitor eros vel dolor. Donec convallis pede venenatis nibh. Duis quam. Nam eget.</p>
    <p class="closing">Thank you for being one of our valued customers.</p>
  </section>

  <div class="signature">
    Name Here<br>
    CEO
  </div>

  <div class="watermark" aria-hidden="true"></div>

  <footer class="footer-band">
    <div class="footer-address">
      215 Larkspur Rd Ste 300,<br>
      Fairview, MD 20990
    </div>
    <div class="contact-lines">
      <div class="contact-line">
        <svg viewBox="0 0 24 24" aria-label="Phone"><path d="M6.6 10.8a15.1 15.1 0 0 0 6.6 6.6l2.2-2.2a1 1 0 0 1 1-.25 11.4 11.4 0 0 0 3.6.57 1 1 0 0 1 1 1V20a1 1 0 0 1-1 1A17 17 0 0 1 3 4a1 1 0 0 1 1-1h3.5a1 1 0 0 1 1 1c0 1.25.2 2.45.57 3.57a1 1 0 0 1-.25 1z"/></svg>
        <span>555-010-4421</span>
      </div>
      <div class="contact-line">
        <svg viewBox="0 0 24 24" aria-label="Fax"><path d="M6 2h12v6H6zM4 9h16a2 2 0 0 1 2 2v7h-4v4H6v-4H2v-7a2 2 0 0 1 2-2zm4 7v4h8v-4z"/></svg>
        <span>555-010-4422</span>
      </div>
    </div>
  </footer>
</main>
</body>
</html>
```